Create a new business card

I’m looking to update my business card to make it match the rest of my brand. I will include my current website as well as what my vehicle designs look like, etc..
What my business currently services
Weekly maintenance pool openings / closings
Equipment repair, including pumps, heaters, salt systems, filters, etc.
We install automatic covers and maintain them as well as provide preventative maintenance

I would like to include my name.
Darren Holcott.
My title
Owner
My email
Darren@tidewellnx.com
4015867120
Www.tidewellnx.com

```html
<!DOCTYPE html>
<html lang="en">
<head>
<meta charset="utf-8">
<title>Tidewell Pool Service – Business Card</title>
<link rel="stylesheet" href="https://fonts.googleapis.com/css2?family=Poppins:wght@400;500;600;700&display=swap">
<style>
  :root {
    --navy: #1f2f66;
    --sky: #29b6e8;
    --orange: #e8672a;
    --white: #ffffff;
    --stage: #d9dbe0;
  }
  * { margin: 0; padding: 0; box-sizing: border-box; }
  html, body { width: 1200px; height: 689px; overflow: hidden; }
  body {
    background: var(--stage);
    font-family: "Poppins", sans-serif;
    position: relative;
  }
  .card {
    position: absolute;
    top: 190px;
    width: 540px;
    height: 309px;
    border-radius: 16px;
    overflow: hidden;
    box-shadow: 0 8px 24px rgba(0,0,0,0.18);
  }
  .brand-dot {
    flex: 0 0 auto;
    width: 26px; height: 26px; border-radius: 50%;
    background: var(--sky);
  }
  .brand-name { font-weight: 600; line-height: 1.15; }

  /* Back card */
  .card-back { left: 40px; background: var(--navy); color: var(--white); }
  .brand-back {
    position: absolute;
    left: 34px; top: 120px;
    width: 190px;
    display: flex; align-items: center; gap: 10px;
  }
  .card-back .brand-name { color: var(--white); font-size: 20px; }
  .services {
    position: absolute;
    left: 250px; top: 36px;
    list-style: none;
  }
  .services li {
    display: flex; align-items: center; gap: 8px;
    font-size: 12.5px;
    line-height: 18px;
    font-weight: 400;
  }
  .tick { width: 11px; height: 11px; flex: 0 0 auto; }

  /* Front card */
  .card-front { left: 620px; background: var(--navy); }
  .front-shape { position: absolute; inset: 0; }
  .brand-front {
    position: absolute;
    left: 186px; top: 56px;
    width: 128px; height: 108px;
    display: flex; flex-direction: column; align-items: center; justify-content: center;
    gap: 6px;
    text-align: center;
  }
  .brand-front .brand-dot { width: 20px; height: 20px; }
  .card-front .brand-name { color: var(--navy); font-size: 15px; }
  .person {
    position: absolute;
    right: 222px; top: 226px;
    text-align: right;
    white-space: nowrap;
  }
  .person-name {
    color: var(--navy);
    font-weight: 700;
    font-size: 24px;
    line-height: 1.1;
  }
  .person-title {
    color: var(--orange);
    font-weight: 500;
    font-size: 14px;
  }
  .divider {
    position: absolute;
    left: 330px; top: 198px;
    width: 2px; height: 78px;
    background: var(--navy);
  }
  .contacts {
    position: absolute;
    left: 344px; top: 196px;
    list-style: none;
    color: var(--navy);
  }
  .contacts li {
    display: flex; align-items: center; gap: 7px;
    font-size: 13px;
    line-height: 26px;
    white-space: nowrap;
  }
  .contacts .phone { font-weight: 600; font-size: 17px; }
  .icon { width: 12px; height: 12px; flex: 0 0 auto; }
</style>
</head>
<body>

<section class="card card-back" aria-label="Card back">
  <div class="brand-back">
    <span class="brand-dot"></span>
    <span class="brand-name">Tidewell Pool Service</span>
  </div>
  <ul class="services">
    <li><svg class="tick" viewBox="0 0 12 12"><circle cx="6" cy="6" r="6" fill="#29b6e8"/><path d="M3.2 6.2l1.9 1.9 3.7-3.9" stroke="#fff" stroke-width="1.6" fill="none"/></svg>Weekly Pool Maintenance</li>
    <li><svg class="tick" viewBox="0 0 12 12"><circle cx="6" cy="6" r="6" fill="#29b6e8"/><path d="M3.2 6.2l1.9 1.9 3.7-3.9" stroke="#fff" stroke-width="1.6" fill="none"/></svg>Pool Opening &amp; Closing</li>
    <li><svg class="tick" viewBox="0 0 12 12"><circle cx="6" cy="6" r="6" fill="#29b6e8"/><path d="M3.2 6.2l1.9 1.9 3.7-3.9" stroke="#fff" stroke-width="1.6" fill="none"/></svg>Equipment Servicing</li>
    <li><svg class="tick" viewBox="0 0 12 12"><circle cx="6" cy="6" r="6" fill="#29b6e8"/><path d="M3.2 6.2l1.9 1.9 3.7-3.9" stroke="#fff" stroke-width="1.6" fill="none"/></svg>Equipment Installation</li>
    <li><svg class="tick" viewBox="0 0 12 12"><circle cx="6" cy="6" r="6" fill="#29b6e8"/><path d="M3.2 6.2l1.9 1.9 3.7-3.9" stroke="#fff" stroke-width="1.6" fill="none"/></svg>Structural Pool Repair</li>
    <li><svg class="tick" viewBox="0 0 12 12"><circle cx="6" cy="6" r="6" fill="#29b6e8"/><path d="M3.2 6.2l1.9 1.9 3.7-3.9" stroke="#fff" stroke-width="1.6" fill="none"/></svg>Plumbing Updates &amp; Upgrades</li>
    <li><svg class="tick" viewBox="0 0 12 12"><circle cx="6" cy="6" r="6" fill="#29b6e8"/><path d="M3.2 6.2l1.9 1.9 3.7-3.9" stroke="#fff" stroke-width="1.6" fill="none"/></svg>Coping Replacement &amp; Removal</li>
    <li><svg class="tick" viewBox="0 0 12 12"><circle cx="6" cy="6" r="6" fill="#29b6e8"/><path d="M3.2 6.2l1.9 1.9 3.7-3.9" stroke="#fff" stroke-width="1.6" fill="none"/></svg>Tile Replacement &amp; Removal</li>
    <li><svg class="tick" viewBox="0 0 12 12"><circle cx="6" cy="6" r="6" fill="#29b6e8"/><path d="M3.2 6.2l1.9 1.9 3.7-3.9" stroke="#fff" stroke-width="1.6" fill="none"/></svg>Interior Resurfacing/Replastering</li>
    <li><svg class="tick" viewBox="0 0 12 12"><circle cx="6" cy="6" r="6" fill="#29b6e8"/><path d="M3.2 6.2l1.9 1.9 3.7-3.9" stroke="#fff" stroke-width="1.6" fill="none"/></svg>Filter System Equipment Upgrades</li>
    <li><svg class="tick" viewBox="0 0 12 12"><circle cx="6" cy="6" r="6" fill="#29b6e8"/><path d="M3.2 6.2l1.9 1.9 3.7-3.9" stroke="#fff" stroke-width="1.6" fill="none"/></svg>Decking Removal &amp; Renovation</li>
    <li><svg class="tick" viewBox="0 0 12 12"><circle cx="6" cy="6" r="6" fill="#29b6e8"/><path d="M3.2 6.2l1.9 1.9 3.7-3.9" stroke="#fff" stroke-width="1.6" fill="none"/></svg>Commercial Pool Services</li>
  </ul>
</section>

<section class="card card-front" aria-label="Card front">
  <svg class="front-shape" viewBox="0 0 540 309" preserveAspectRatio="none">
    <path d="M40 309 C95 170 280 78 540 56 L540 70 C285 92 106 176 54 309 Z" fill="#29b6e8"/>
    <path d="M58 309 C110 176 285 90 540 74 L540 80 C288 98 118 184 66 309 Z" fill="#e8672a"/>
    <path d="M70 309 C120 180 290 100 540 88 L540 309 Z" fill="#ffffff"/>
    <circle cx="250" cy="110" r="68" fill="#ffffff"/>
  </svg>
  <div class="brand-front">
    <span class="brand-dot"></span>
    <span class="brand-name">Tidewell Pool Service</span>
  </div>
  <div class="person">
    <p class="person-name">Darren Holcott</p>
    <p class="person-title">Owner</p>
  </div>
  <div class="divider"></div>
  <ul class="contacts">
    <li class="phone"><svg class="icon" viewBox="0 0 12 12"><path d="M2.5 1l2 2.3-1.1 1.4c.7 1.5 1.8 2.6 3.2 3.3l1.4-1.1L10.3 9 9 10.8C5 10.5 1.5 7 1.2 2.8Z" fill="#29b6e8"/></svg>(401) 586-7120</li>
    <li><svg class="icon" viewBox="0 0 12 12"><rect x="0.5" y="2.5" width="11" height="7.5" rx="1" fill="#29b6e8"/><path d="M1 3l5 3.6L11 3" stroke="#fff" stroke-width="1" fill="none"/></svg>Darren@tidewellnx.com</li>
    <li><svg class="icon" viewBox="0 0 12 12"><circle cx="6" cy="6" r="5.2" fill="none" stroke="#29b6e8" stroke-width="1.3"/><ellipse cx="6" cy="6" rx="2.2" ry="5.2" fill="none" stroke="#29b6e8" stroke-width="1"/><path d="M1 6h10" stroke="#29b6e8" stroke-width="1"/></svg>Www.tidewellnx.com</li>
  </ul>
</section>

</body>
</html>
```